Bright Lantern Studios Business Card Design

Doug Farley

Managing Partner

Doug@BrightLanternStudios.com

BrightLanternStudios.com

502-417-2356

Industry/Entity Type

Photographer

Contact Information for Business Card

Doug Farley

Managing Partner

Doug@BrightLanternStudios.com

BrightLanternStudios.com

502-417-2356

Requirements
Must have
• Must show that I am a pavlo trusted photographer

```html
<!DOCTYPE html>
<html lang="en">
<head>
<meta charset="UTF-8">
<title>Bright Lantern Studios Business Card</title>
<link rel="stylesheet" href="https://fonts.googleapis.com/css2?family=Josefin+Sans:wght@400;600&family=Roboto:wght@400&display=swap">
<style>
  :root {
    --page-bg: #2e2e2e;
    --card-front: #0b0b0b;
    --card-front-glow: #1a1a1a;
    --card-back: #ffffff;
    --ink-light: #f2f2f2;
    --ink-soft: #d6d6d6;
    --ink-dark: #111111;
    --badge-gold: #f6b21b;
    --divider: #cfcfcf;
  }
  * { margin: 0; padding: 0; box-sizing: border-box; }
  html, body {
    width: 1200px;
    height: 960px;
    overflow: hidden;
    background: var(--page-bg);
  }
  .canvas {
    position: relative;
    width: 1200px;
    height: 960px;
  }
  .card {
    position: absolute;
    left: 358px;
    width: 487px;
    height: 282px;
    box-shadow: 0 3px 6px rgba(0,0,0,0.55);
  }
  .card-front {
    top: 175px;
    background: radial-gradient(ellipse at 50% 35%, var(--card-front-glow) 0%, var(--card-front) 70%);
  }
  .card-back {
    top: 505px;
    height: 280px;
    background: var(--card-back);
  }
  .identity {
    position: absolute;
    right: 262px;
    top: 117px;
    text-align: right;
    color: var(--ink-light);
  }
  .identity-name {
    font-family: "Josefin Sans", sans-serif;
    font-weight: 400;
    font-size: 22px;
    letter-spacing: 0.3px;
    line-height: 26px;
    text-transform: uppercase;
  }
  .identity-role {
    font-family: "Roboto", sans-serif;
    font-size: 11px;
    line-height: 14px;
    color: var(--ink-soft);
    margin-top: 1px;
  }
  .divider {
    position: absolute;
    left: 243px;
    top: 117px;
    width: 1px;
    height: 42px;
    background: var(--divider);
  }
  .contact-list {
    position: absolute;
    left: 261px;
    top: 116px;
    list-style: none;
    font-family: "Roboto", sans-serif;
    font-size: 12px;
    color: var(--ink-light);
  }
  .contact-item {
    display: flex;
    align-items: center;
    height: 15.5px;
  }
  .contact-icon {
    width: 10px;
    height: 10px;
    margin-right: 6px;
    fill: var(--ink-soft);
    flex-shrink: 0;
  }
  .brand {
    position: absolute;
    left: 0;
    right: 0;
    top: 82px;
    text-align: center;
  }
  .brand-dot {
    display: block;
    width: 34px;
    height: 34px;
    margin: 0 auto 36px;
    border-radius: 50%;
    background: var(--ink-dark);
  }
  .brand-name {
    font-family: "Josefin Sans", sans-serif;
    font-weight: 600;
    font-size: 24px;
    letter-spacing: 0.5px;
    color: var(--ink-dark);
    text-transform: uppercase;
  }
  .trust-badge {
    position: absolute;
    left: 179px;
    top: 212px;
    width: 124px;
    height: 42px;
    border-radius: 6px;
    background: var(--badge-gold);
  }
</style>
</head>
<body>
<main class="canvas">
  <section class="card card-front" aria-label="Business card front">
    <div class="identity">
      <p class="identity-name">Doug Farley</p>
      <p class="identity-role">Managing Partner</p>
    </div>
    <span class="divider"></span>
    <ul class="contact-list">
      <li class="contact-item">
        <svg class="contact-icon" viewBox="0 0 10 10" aria-hidden="true"><path d="M2 0.5 L3.6 0.5 L4.3 2.8 L3.1 3.7 C3.7 5 4.9 6.2 6.3 6.9 L7.2 5.7 L9.5 6.4 L9.5 8 C9.5 9 8.7 9.6 7.8 9.5 C4 9 1 6 0.5 2.2 C0.4 1.3 1 0.5 2 0.5 Z"/></svg>
        502-417-2356
      </li>
      <li class="contact-item">
        <svg class="contact-icon" viewBox="0 0 10 10" aria-hidden="true"><path d="M0.5 2 H9.5 V8.5 H0.5 Z M1.2 2.6 L5 5.6 L8.8 2.6 Z" fill-rule="evenodd"/></svg>
        Doug@BrightLanternStudios.com
      </li>
      <li class="contact-item">
        <svg class="contact-icon" viewBox="0 0 10 10" aria-hidden="true"><circle cx="5" cy="5" r="4.3" fill="none" stroke="#d6d6d6" stroke-width="0.9"/><ellipse cx="5" cy="5" rx="1.8" ry="4.3" fill="none" stroke="#d6d6d6" stroke-width="0.8"/><path d="M0.8 5 H9.2" stroke="#d6d6d6" stroke-width="0.8"/></svg>
        www.BrightLanternStudios.com
      </li>
    </ul>
  </section>

  <section class="card card-back" aria-label="Business card back">
    <div class="brand">
      <span class="brand-dot"></span>
      <p class="brand-name">Bright Lantern Studios</p>
    </div>
    <div class="trust-badge" role="img" aria-label="Pavlo trusted photographer badge"></div>
  </section>
</main>
</body>
</html>
```